zunTRAK Company Website
Technology Solutions and Consulting
Project: zunTRAK Company Website
zunTRAK Company Website - Information Technology
Creative Brief
Information Technology
www.zuntrak.net
We offer Technology, Telecom Services, Solutions and Consulting for enterprise level businesses. Specializing but not limited to telecom related businesses. zunTRAK is an integrated business development solution company that provides technology integration, advisory services, infrastructure to enterprises and SME to boost their leads, sales and customers satisfactions. zunTRAK provide the following solutions :
- Digital Marketing Solutions (mobile, internet) for enterprise/SMEs to help them promote/boost their business by generating leads, increasing sales and customers satisfactions.
- Telecom innovative solutions to help operators better their time to market and products and services portfolio
- Consultancy services for businesses: creates tactical programs to help businesses boost their bottom-line.
- Local business, products and service search engines for Africa region.
- Payments & cash-less solutions.
zunTRAK has a couple of subrands: KeloBridge: which is a digital marketing Offering zunSHOP: local business, products and services database and search engine Vision & Philosophy
The companys goal is to create long-term shareholder value by enhancing its position as a leading solution provider. The company’s philosophy focuses on end user experience through feedback, innovation, teamwork and integrity.
Something modern, cutting edge, but VERY professional. These are the pages required: HOME ABOUT US SERVICES OFFERING SOLUTIONS INDUSTRIES COVERED TECHNOLOGY & PARTNERS KELOBRIDGE KELOSHOP ZUNCAST
Blue
Grey / Silver
White / Black
left side
http://art.pictoquill.com/drafts/display/contest/118240/draft/3faa92c1d7e04b58a1c6f0d2b7e95a4c61830
http://art.pictoquill.com/drafts/display/contest/927615/draft/b81c44e09fa3d27c5e6018a9d4c7f2e390451
http://www.terubelmo.com/
Want something sleek, modern, cutting edge and professional. Open to suggestions. Will modify comments as I see a few websites come in. Love the modern look of our Logo designed attached. The website should be 2 languages: French and English. I have provided the menu in the 2 languages.

```html
<!DOCTYPE html>
<html lang="en">
<head>
<meta charset="utf-8">
<title>ZUNTRAK – Technology, Telecom, Consulting</title>
<link href="https://fonts.googleapis.com/css2?family=Open+Sans:wght@400;600;700&family=Oswald:wght@500&display=swap" rel="stylesheet">
<style>
:root{
  --navy:#14235a;
  --navy-2:#1c3277;
  --blue:#1f5fb4;
  --sky-top:#bcd6ef;
  --sky-bottom:#eef4fa;
  --panel:#ffffff;
  --grey:#e7e9ee;
  --grey-dark:#8a8f99;
  --text:#333a45;
  --white:#ffffff;
}
*{box-sizing:border-box;margin:0;padding:0}
html,body{width:1200px;height:885px;overflow:hidden}
body{font-family:"Open Sans",Arial,sans-serif;color:var(--text);
  background:linear-gradient(180deg,var(--sky-top) 0,#d8e7f5 380px,var(--sky-bottom) 885px);position:relative}
a{color:inherit;text-decoration:none}
.page{position:absolute;left:228px;top:0;width:744px;height:885px}

/* header */
.brand{position:absolute;left:6px;top:14px}
.brand-name{font-size:38px;font-weight:700;color:var(--navy-2);line-height:1;letter-spacing:1px}
.brand-tag{position:absolute;left:8px;top:52px;font-size:11px;color:var(--blue);white-space:nowrap}
.topbar{position:absolute;left:248px;top:0;width:496px;height:22px;background:var(--navy);
  color:var(--white);font-size:11px;font-weight:700;display:flex;align-items:center;padding:0 0 0 10px;gap:14px}
.topbar .sep{margin-left:auto}
.topbar .btn{padding:0 12px;border-left:1px solid #3b4c86}
.lang{position:absolute;left:442px;top:30px;font-size:11px;font-weight:700;color:var(--navy);display:flex;gap:6px;align-items:center}
.flag{width:16px;height:11px;display:inline-block}
.util{position:absolute;right:12px;top:30px;font-size:10px;color:var(--navy);display:flex;gap:10px}
.search{position:absolute;right:12px;top:50px;width:156px;height:18px;background:var(--white);
  border:1px solid #9bb0cc;font-size:9px;color:var(--grey-dark);padding:2px 6px}

/* hero */
.sidenav{position:absolute;left:0;top:100px;width:216px;height:296px;
  background:linear-gradient(180deg,var(--navy-2),var(--navy));padding:20px 0 0 20px;border-radius:6px 0 0 6px}
.sidenav li{list-style:none;font-size:12px;font-weight:600;color:var(--white);height:26px;display:flex;align-items:center;
  border-bottom:1px solid #2c428a;width:176px}
.sidenav li::before{content:"";width:0;height:0;border-left:5px solid #8fb4e8;border-top:4px solid transparent;border-bottom:4px solid transparent;margin-right:8px}
.slide{position:absolute;left:218px;top:84px;width:526px;height:276px;
  background:linear-gradient(135deg,#f4f6f8 0,#dfe6ee 45%,#b9c7d6 100%);border-radius:0 6px 0 0}
.slide-dots{position:absolute;right:14px;bottom:8px;display:flex;gap:5px}
.slide-dots i{width:6px;height:6px;border-radius:50%;background:#9aa9bb}
.slide-bar{position:absolute;left:218px;top:360px;width:526px;height:36px;background:var(--navy);border-radius:0 0 6px 0}
.slide-bar a{position:absolute;right:18px;top:11px;font-size:11px;color:var(--white);text-decoration:underline}

/* content */
.content{position:absolute;left:0;top:403px;width:744px;height:353px;background:var(--panel);border-radius:6px}
.services{position:absolute;left:5px;top:4px;width:200px;height:345px;background:var(--grey);border-radius:4px}
.services h2{font-family:"Oswald",sans-serif;font-size:19px;color:var(--navy-2);padding:10px 0 0 50px;height:50px}
.services .gear{position:absolute;left:12px;top:10px;width:30px;height:30px;border-radius:50%;border:5px solid var(--grey-dark)}
.services ul{list-style:none;padding:4px 4px 0 8px}
.services li{font-size:8.6px;color:var(--text);line-height:23px;padding-left:12px;position:relative;white-space:nowrap}
.services li::before{content:"";position:absolute;left:0;top:9px;width:6px;height:6px;border-radius:50%;background:var(--blue)}
.welcome{position:absolute;left:212px;top:10px;width:524px}
.welcome h1{font-size:19px;font-weight:700;color:var(--blue);padding-left:42px;position:relative;height:32px}
.welcome h1::before{content:"";position:absolute;left:0;top:-2px;width:30px;height:30px;border-radius:50%;background:var(--blue)}
.welcome p{font-size:9.5px;line-height:13px;margin:6px 0 0 0;text-align:justify}
.more{position:absolute;right:10px;top:212px;background:var(--navy);color:var(--white);font-size:10px;font-weight:600;
  padding:3px 10px;border-radius:10px}
.box{position:absolute;top:226px;width:228px;height:123px;background:var(--grey);border-radius:4px 4px 0 0;text-align:center}
.box h3{background:var(--navy);color:var(--white);font-size:14px;font-weight:700;height:26px;line-height:26px;border-radius:4px 4px 0 0}
.box li{list-style:none;font-size:9px;font-weight:600;color:var(--navy);line-height:22px;border-bottom:1px solid #d0d4dc;margin:0 10px}
.box.sms{left:252px}.box.web{left:492px}

/* footer */
.footer{position:absolute;left:0;top:763px;width:744px;height:100px;background:var(--panel);border-radius:6px}
.flinks{font-size:8px;font-weight:600;color:var(--navy);text-align:center;padding-top:8px;border-bottom:1px solid #d8dce4;padding-bottom:6px;margin:0 12px}
.fbrand{position:absolute;left:22px;top:44px;font-size:24px;font-weight:700;color:var(--grey-dark);letter-spacing:1px}
.social{position:absolute;left:300px;top:36px;text-align:center;width:130px}
.social h4{font-size:13px;font-weight:700;color:var(--navy)}
.social div{display:flex;gap:6px;justify-content:center;margin-top:6px}
.social i{width:20px;height:20px;border-radius:50%;background:var(--navy)}
.signup{position:absolute;left:470px;top:36px}
.signup h4{font-size:13px;font-weight:700;color:var(--navy)}
.signup input{width:160px;height:22px;border:1px solid #b3bccb;margin-top:6px;vertical-align:middle}
.signup button{height:22px;background:var(--navy);color:var(--white);font-size:11px;font-weight:700;border:0;padding:0 10px;margin-left:4px;vertical-align:middle;font-family:inherit}
.copy{position:absolute;left:0;top:866px;width:744px;text-align:center;font-size:10px;color:var(--navy)}
</style>
</head>
<body>
<div class="page">
  <header>
    <div class="brand"><span class="brand-name">ZUNTRAK</span></div>
    <div class="brand-tag">Technology . Telecom . Consulting</div>
    <div class="topbar"><span>INFO@ZUNTRAK.NET</span><span>+000 00 00 01 / +000 00 00 02</span><span class="sep btn">LOGIN</span><span class="btn">REGISTER</span></div>
    <div class="lang">LANGUAGE
      <svg class="flag" viewBox="0 0 16 11"><rect width="16" height="11" fill="#1f3a8a"/><path d="M0 0L16 11M16 0L0 11" stroke="#fff" stroke-width="2"/><path d="M8 0V11M0 5.5H16" stroke="#c8102e" stroke-width="2"/></svg>
      <svg class="flag" viewBox="0 0 16 11"><rect width="5.3" height="11" fill="#1f3a8a"/><rect x="5.3" width="5.4" height="11" fill="#fff"/><rect x="10.7" width="5.3" height="11" fill="#c8102e"/></svg>
    </div>
    <nav class="util"><a href="#">Home</a><a href="#">Careers</a><a href="#">Contact Us</a></nav>
    <div class="search">ADVANCE SEARCH</div>
  </header>

  <nav class="sidenav"><ul>
    <li>HOME</li><li>ABOUT US</li><li>SERVICES OFFERING</li><li>SOLUTIONS</li><li>INDUSTRIES COVERED</li>
    <li>TECHNOLOGY &amp; PARTNERS</li><li>KELOBRIDGE</li><li>KELOSHOP</li><li>ZUNCAST</li>
  </ul></nav>
  <div class="slide" role="img" aria-label="Photo of business people working with a tablet and charts on a desk">
    <div class="slide-dots"><i></i><i></i><i></i></div>
  </div>
  <div class="slide-bar"><a href="#">BOARD OF DIRECTORS</a></div>

  <main class="content">
    <section class="services">
      <span class="gear"></span>
      <h2>OUR SERVICES</h2>
      <ul>
        <li>Construction of customer base by SMS</li>
        <li>Customer Loyalty SMS</li>
        <li>Manage your appointments by SMS</li>
        <li>Bring your customers</li>
        <li>Telecom Value Added Solutions</li>
        <li>Mobile Money/banking</li>
        <li>Telecom Value Added Delivery Platform</li>
        <li>Telecom Services Quality Testing</li>
        <li style="padding-left:12px">&amp; Monitoring</li>
        <li>Digital Marketing</li>
      </ul>
    </section>
    <section class="welcome">
      <h1>WELCOME TO OUR SITE....</h1>
      <p>zunTRAK is a technology company focused on Value Added Solutions delivery in the Enterprise space and Information Technology Consulting. zunTRAK draws from an experienced base of personnel whilst maintaining a personalized form of business liaison. The ultimate in consultation, skills diversity and adaptability to meet client expectations are the very strengths of zunTRAK. It is based in Tenkoro, Kelonia and managed by a team of young professionals within and outside Kelonia who have acquired a vast wealth of relevant industry experience. We are positioned as key solution consultants, developing strategic relationships with technology and solution providers.</p>
      <p>At zunTRAK, our focus is to enable our customers achieve a competitive advantage by the strategic and cost-effective solution of technological innovation to their business processes. Our solutions span a range of industry standards and platforms targeted at adding immediate value to the client.</p>
    </section>
    <a class="more" href="#">Read More</a>
    <section class="box sms"><h3>SMS MARKETING</h3><ul>
      <li>Multi-channel digital marketing</li><li>Communication campaigns</li><li>Confirmations of appointment</li><li>SMS, Internet and social networks</li>
    </ul></section>
    <section class="box web"><h3>WEB SOLUTION</h3><ul>
      <li>zunTRAK accommodation</li><li>zunTRAK website development</li><li>zunTRAK web interface consultation</li><li>After sales services for websites</li>
    </ul></section>
  </main>

  <footer class="footer">
    <div class="flinks">HOME &nbsp;|&nbsp; ABOUT US &nbsp;|&nbsp; SERVICES OFFERING &nbsp;|&nbsp; SOLUTIONS &nbsp;|&nbsp; INDUSTRIES COVERED &nbsp;|&nbsp; TECHNOLOGY &amp; PARTNERS &nbsp;|&nbsp; KELOBRIDGE &nbsp;|&nbsp; KELOSHOP &nbsp;|&nbsp; ZUNCAST</div>
    <div class="fbrand">ZUNTRAK</div>
    <div class="social"><h4>STAY CONNECTED</h4><div><i></i><i></i><i></i><i></i></div></div>
    <form class="signup"><h4>SIGN UP TO JOIN US</h4><input type="text" aria-label="Email"><button type="button">SUBMIT »</button></form>
  </footer>
  <div class="copy">© 2013. zunTRAK</div>
</div>
</body>
</html>
```